Ardenwell Building and Property Services needs a business card design

We need a business card design for our building and property services business. We already have a logo we just need a creative design and layout on a business card. Emphasis on clean, modern, professional.
Our client targets are mainly body corporates, building managers, construction managers.
We are a building services company that lean more to structural repair of buildings, through concrete rectification and carbon fibre strengthening.
We also refurbish facades, rendering, painting etc
We target higher end body corporates in prestigious locations, hence why we'd like our cards to reflect professionalism, strength, efficiency

Target Market(s)

body corporates, building managers, construction managers

Industry/Entity Type

Construction

Contact Information for Business Card

Ardenwell is the main word, with 'Building and Property Services' underneath.
Level 17, 82 Harlow Street
MERRIDALE
Melbourne
Vic 3094
T: 9518 2736
Duncan Ferris - Director
dunardenwell@mailbox-example.com

Requirements
Must have
• Stand out on the back of the card- strong/ bold, company logo
• All of the contact details written above
Should not have
• I'd like the card to stand out, especially on the back. Id like the company logo to be prominent, although feel free to be creative around it. But remain clean and professional

```html
<!DOCTYPE html>
<html lang="en">
<head>
<meta charset="utf-8">
<title>Ardenwell Building and Property Services – Business Card</title>
<link rel="stylesheet" href="https://fonts.googleapis.com/css2?family=Cinzel:wght@400;600&family=Open+Sans:wght@400;600&display=swap">
<style>
  :root {
    --stage: #1b1918;
    --card: #1e1f21;
    --card-back: #232426;
    --band-light: #f2f2f2;
    --band-mid: #c9cacc;
    --band-dark: #9a9b9e;
    --ink: #2a2a2a;
    --brand-blue: #2f8fe0;
    --brand-blue-deep: #1d6fc0;
    --emboss: #8d8f93;
  }
  * { margin: 0; padding: 0; box-sizing: border-box; }
  html, body {
    width: 1200px; height: 716px; overflow: hidden;
    background: var(--stage);
    font-family: "Open Sans", Arial, sans-serif;
  }
  .canvas {
    position: relative; width: 1200px; height: 716px;
    display: flex; align-items: center; justify-content: center; gap: 40px;
  }
  .card {
    position: relative; width: 520px; height: 300px;
    border-radius: 3px; overflow: hidden;
    box-shadow: 0 14px 30px rgba(0,0,0,.55);
  }
  .card--front { background: var(--card); }
  .card--back {
    background: var(--card-back);
    display: flex; align-items: center; justify-content: center;
  }

  .silver-band {
    position: absolute; left: 0; right: 0; top: 54px; height: 118px;
    background: linear-gradient(180deg, var(--band-light) 0%, var(--band-mid) 55%, var(--band-dark) 100%);
  }
  .person {
    position: absolute; left: 22px; top: 68px; color: var(--ink);
  }
  .person__name {
    font-family: "Cinzel", Georgia, serif; font-size: 15px; font-weight: 400;
    font-variant: small-caps; letter-spacing: .5px;
  }
  .person__role {
    font-size: 8px; font-weight: 600; letter-spacing: 1px; margin-top: 3px;
  }

  .contact {
    position: absolute; right: 20px; top: 82px; text-align: right;
    color: var(--ink); font-size: 9.5px; line-height: 15px;
  }
  .contact__row { display: flex; align-items: center; justify-content: flex-end; gap: 6px; }
  .contact__icon { width: 10px; height: 10px; }
  .contact__spacer { display: inline-block; width: 10px; }

  .wordmark {
    position: absolute; left: 0; right: 0; top: 186px; text-align: center;
  }
  .wordmark__name {
    display: inline-flex; align-items: center; gap: 12px;
    font-family: "Cinzel", Georgia, serif; font-weight: 600;
    font-size: 40px; letter-spacing: 3px; color: var(--brand-blue);
  }
  .wordmark__square {
    width: 14px; height: 14px; background: var(--brand-blue);
  }
  .wordmark__tagline {
    font-family: "Cinzel", Georgia, serif; font-size: 10px; letter-spacing: 2.6px;
    color: var(--brand-blue-deep); text-transform: uppercase; margin-top: 4px;
  }

  .back-mark {
    display: inline-flex; align-items: center; gap: 16px;
    font-family: "Cinzel", Georgia, serif; font-weight: 600;
    font-size: 44px; letter-spacing: 4px; color: var(--emboss);
  }
  .back-mark__square {
    width: 16px; height: 16px; border: 2px solid var(--emboss);
  }
</style>
</head>
<body>
<main class="canvas">
  <section class="card card--front" aria-label="Card front">
    <div class="silver-band"></div>

    <div class="person">
      <p class="person__name">Duncan Ferris</p>
      <p class="person__role">DIRECTOR</p>
    </div>

    <address class="contact">
      <div class="contact__row">9518 2736
        <svg class="contact__icon" viewBox="0 0 10 10" aria-hidden="true">
          <rect width="10" height="10" rx="1.5" fill="#2a2a2a"/>
          <path d="M3 2.2 L4.2 3.6 L3.6 4.3 Q4.3 5.7 5.7 6.4 L6.4 5.8 L7.8 7 L7 7.9 Q4 7.6 2.1 3 Z" fill="#eee"/>
        </svg>
      </div>
      <div class="contact__row">dunardenwell@mailbox-example.com
        <svg class="contact__icon" viewBox="0 0 10 10" aria-hidden="true">
          <rect width="10" height="10" rx="1.5" fill="#2a2a2a"/>
          <rect x="2" y="3" width="6" height="4.2" fill="none" stroke="#eee" stroke-width=".8"/>
          <path d="M2 3 L5 5.4 L8 3" fill="none" stroke="#eee" stroke-width=".8"/>
        </svg>
      </div>
      <div class="contact__row">Level 17, 82 Harlow Street<span class="contact__spacer"></span></div>
      <div class="contact__row">MERRIDALE, Melbourne, Vic 3094<span class="contact__spacer"></span></div>
    </address>

    <div class="wordmark">
      <div class="wordmark__name"><span class="wordmark__square"></span>ARDENWELL</div>
      <p class="wordmark__tagline">Building and Property Services</p>
    </div>
  </section>

  <section class="card card--back" aria-label="Card back">
    <div class="back-mark"><span class="back-mark__square"></span>ARDENWELL</div>
  </section>
</main>
</body>
</html>
```